Redesign of a Brochure based on an exsiting example for Web download and email marketing

Can you create a professional brochure based on the attached PDF. We need to keep the name, the logo and the content but everything else can be changed . The PDF will primarily be will be used for web download and email marking but it aslo be printed out for a poster design will be appropriate

Target Market(s)

Business to Business

Industry/Entity Type

Marketing

Font styles to use
Serif

Requirements
Must have
• Must have the existing logo ( in the attached document) and contain the same content

```html
<!DOCTYPE html>
<html lang="en">
<head>
<meta charset="utf-8">
<title>IT RUN Model 1 – Layer 3 Business View</title>
<link href="https://fonts.googleapis.com/css2?family=Crimson+Text:wght@400;600;700&display=swap" rel="stylesheet">
<style>
  :root{
    --band:#0f7fcb;
    --band-light:#1aa3e0;
    --bg:#d4ecfa;
    --panel:#ffffff;
    --tab:#c9e7f9;
    --pill-border:#8cc6ec;
    --navy:#2b2a78;
    --accent:#1f6fb2;
    --link:#2a6db5;
    --ink:#1c1c1c;
    --yellow:#efe62b;
    --footer:#3a9ad8;
    --icon:#19a3ea;
  }
  *{box-sizing:border-box;margin:0;padding:0}
  html,body{width:1200px;height:848px;overflow:hidden}
  body{font-family:"Crimson Text",serif;background:var(--bg);color:var(--ink);position:relative}
  .abs{position:absolute}
  .top-band{left:0;top:0;width:1200px;height:175px}
  .model-banner{left:0;top:52px;width:402px;height:44px}
  .model-name{left:68px;top:56px;font-size:23px;color:var(--yellow);line-height:34px}
  .brand{left:960px;top:60px;display:flex;align-items:center;gap:10px}
  .brand-dot{width:14px;height:14px;border-radius:50%;background:#fff}
  .brand-name{font-size:28px;font-weight:400;color:#fff;line-height:32px}
  .pill{background:#fff;border:3px solid var(--pill-border);border-radius:14px;display:flex;align-items:center;justify-content:center}
  .title-pill{left:264px;top:112px;width:666px;height:52px;border-radius:18px}
  .title-pill h1{font-size:24px;font-weight:600;color:var(--navy);letter-spacing:.3px}
  .sample-pill{left:540px;top:176px;width:204px;height:36px}
  .sample-pill h2{font-size:23px;font-weight:700;color:var(--accent)}
  .col-pill{top:218px;width:126px;height:35px}
  .col-pill h3{font-size:25px;font-weight:400;color:#111}
  .measure-pill{left:368px}
  .insight-pill{left:800px}
  .connector{left:418px;top:193px;width:445px;height:26px;border:1.5px solid #7fb8df;border-bottom:none}
  .card{background:var(--panel);border-radius:8px}
  .intro-card{left:46px;top:234px;width:280px;height:496px;padding:36px 24px 0 24px}
  .main-panel{left:348px;top:234px;width:806px;height:496px}
  p{font-size:14.2px;line-height:17px;margin-bottom:9px}
  .measure{left:370px;width:230px;background:var(--tab);clip-path:polygon(0 0,88% 0,100% 50%,88% 100%,0 100%);padding:3px 0 0 13px;color:var(--link)}
  .measure .head{font-size:18px;font-weight:700;text-decoration:underline;line-height:22px}
  .measure .item{font-size:13.5px;line-height:17px}
  .m-desktop{top:279px;height:78px}
  .m-email{top:404px;height:40px;padding-top:8px}
  .m-erp{top:492px;height:70px}
  .m-erp .item{font-size:16px;line-height:22px}
  .illus-house{left:370px;top:576px;width:200px;height:154px;background:linear-gradient(160deg,#e6f3fb,#8cc0e4 55%,#2f6fa6);clip-path:polygon(50% 0,100% 28%,100% 100%,0 100%,0 28%)}
  .insight{left:662px;top:270px;width:440px}
  .photo-hands{left:662px;top:646px;width:426px;height:84px;background:linear-gradient(90deg,#b8cde0,#eef3f7 40%,#6b86a6)}
  .footer{left:0;top:760px;width:1200px;height:88px;background:var(--footer)}
  .sources{left:42px;top:780px;color:#fff;font-size:13.5px;line-height:15.5px}
  .sources .label{text-decoration:underline;font-weight:600}
  .icon-box{left:1086px;top:728px;width:80px;height:94px;background:var(--icon);border:2px solid #fff;border-radius:7px;display:flex;align-items:center;justify-content:center}
</style>
</head>
<body>
  <svg class="abs top-band" viewBox="0 0 1200 175" aria-hidden="true">
    <polygon points="0,0 1200,0 1200,175 1148,175 1112,155 88,155 52,175 0,175" fill="var(--band)"/>
  </svg>
  <svg class="abs model-banner" viewBox="0 0 402 44" aria-hidden="true">
    <polygon points="0,0 372,0 402,22 372,44 0,44" fill="var(--band-light)"/>
  </svg>
  <div class="abs model-name">Model Name: IT RUN Model 1</div>

  <div class="abs brand">
    <div class="brand-dot"></div>
    <div class="brand-name">VERACOST</div>
  </div>

  <div class="abs pill title-pill"><h1>LAYER 3 - BUSINESS VIEW : PRODUCTS AND SERVICES</h1></div>

  <div class="abs connector"></div>
  <div class="abs pill sample-pill"><h2>Sample Output</h2></div>

  <div class="abs card intro-card">
    <p>In this model we have added a simple products &amp; services layer that brings together all the costs from the previous layers. It is split into two broad categories, namely Products and Services. Services are owned by the IT organisation and can be sold to the business on a unit priced basis for example, email and desktop services. It is possible to have a Technology Services layer that sells infrastructure by unit costs but these are seldom understood at a business level.</p>
    <p>Products reflect the line of business applications that support the operating business. They always have a business owner and need to be capacity managed in line with business demand. The default categories are fairly generic, although it is possible to extend the model with your own Business Capabilities, maybe starting with industry reference architectures. However, for simplicity this layer has been designed to support Cost management, Vendor management, and Business demand.</p>
  </div>

  <div class="abs card main-panel"></div>
  <div class="abs pill col-pill measure-pill"><h3>Measure</h3></div>
  <div class="abs pill col-pill insight-pill"><h3>Insight</h3></div>

  <div class="abs measure m-desktop">
    <div class="head">Desktop</div>
    <div class="item">Cost per Desktop PC - Thin Client</div>
    <div class="item">Cost Desktop PC - Thick Client</div>
    <div class="item">Cost per Laptop PC</div>
  </div>
  <div class="abs measure m-email">
    <div class="head"><span>Email</span><span style="text-decoration:none"> Cost Per Mailbox</span></div>
  </div>
  <div class="abs measure m-erp">
    <div class="head">ERP</div>
    <div class="item">ERP cost per user</div>
    <div class="item">ERP cost per transaction</div>
  </div>

  <div class="abs illus-house" role="img" aria-label="Illustration of an email symbol above a data landscape in blue tones"></div>

  <div class="abs insight">
    <p>Desktop is a typical service that is owned by the IT organisation and sold back to the business. The three categories here represent the fully loaded cost of providing these services. These often include costs that are not evident to the business such as break fix maintenance, set-up and support costs. Thin client solutions typically have datacentre, server and software costs that are needed to support the desktop virtualisation. These costs should be offset by reduced desktop support staff costs.</p>
    <p>Email is another service that is owned by the IT organisation and sold back to the business. It is not a differentiator but it is critical to nearly all business operations. It is important to include performance criteria in this category, such as SLA and amount of storage to make valid cost for performance comparisons.</p>
    <p>This is the first foray into products that support particular business processes. Here we look at ERP cost per user but also ERP cost per transaction – focus on transaction costs begins to show the business the cost of supporting their processes and we can start to manage capacity and demand. For example, the business may be using three separate applications to support the same process. In highlighting the costs there could be a case for consolidation / rationalisation (for example across a preferred channel) or indeed a case for further investment.</p>
  </div>

  <div class="abs photo-hands" role="img" aria-label="Photo of a business person's hands writing with a pen beside a coffee cup"></div>

  <div class="abs footer"></div>
  <div class="abs sources">
    <div class="label">Data sources</div>
    <div>1. Layer 1 and Layer 2</div>
    <div>2. Business Usage Data</div>
  </div>

  <div class="abs icon-box">
    <svg width="44" height="72" viewBox="0 0 44 72" aria-hidden="true">
      <rect x="15" y="4" width="14" height="46" rx="7" fill="none" stroke="#111" stroke-width="3"/>
      <circle cx="22" cy="58" r="11" fill="#111"/>
      <rect x="19" y="24" width="6" height="30" fill="#111"/>
      <g stroke="#111" stroke-width="2">
        <line x1="3" y1="10" x2="12" y2="10"/><line x1="32" y1="10" x2="41" y2="10"/>
        <line x1="3" y1="17" x2="12" y2="17"/><line x1="32" y1="17" x2="41" y2="17"/>
        <line x1="3" y1="24" x2="12" y2="24"/><line x1="32" y1="24" x2="41" y2="24"/>
        <line x1="3" y1="31" x2="12" y2="31"/><line x1="32" y1="31" x2="41" y2="31"/>
        <line x1="3" y1="38" x2="12" y2="38"/><line x1="32" y1="38" x2="41" y2="38"/>
      </g>
    </svg>
  </div>
</body>
</html>
```